Calendar Ad / Flyer

Our law firm needs a calendar ad to place in a local calendar.
THE DEADLINE IS THIS THURSDAY 06/28/2018.

Attached is the ad used in last years calendar. A few notes on this...
**. This is by no means the model to follow.
Please be creative and do what makes more sense marketing wise.
1. Need to update the color scheme which corresponds to the new website at marvolinlegal.com
2. The "MARVOLIN LAW | SHAPING FAITH WITH RESULTS" should be put at the top and made larger
3. "KNOWN AND TRUSTED IN OUR COMMUNITY FOR OVER 21 YEARS" should be changed to "KNOWN AND TRUSTED IN OUR COMMUNITY FOR OVER 22 YEARS"
4. "Gordon R. Marvolin, Esq." should be made larger and better positioned.
5. Under the list of practices, it should be changed to have:
"Personal Injury, Legal Malpractice, Unlicensed Contractors, Medical Malpractice, Civil Litigation"
6. Contact information (i.e. contact number, website, and address) should be better positioned
7. Placement of endorsement logos should stand out more.
8. New picture of head attorney is attached.

Last but not least... Give it your best shot!

```html
<!DOCTYPE html>
<html lang="en">
<head>
<meta charset="utf-8">
<title>Marvolin Law – Calendar Ad</title>
<link rel="stylesheet" href="https://fonts.googleapis.com/css2?family=Montserrat:ital,wght@0,400;0,500;0,600;1,500;1,800&family=Tinos:ital,wght@1,700&display=swap">
<style>
  :root {
    --ink-dark: #1c1c1c;
    --city-top: #3a3a3a;
    --city-bottom: #151515;
    --gold: #c9a46c;
    --gold-band: #c6a26e;
    --white: #ffffff;
    --grey-text: #d4d4d4;
    --band-text: #2a2520;
    --suit-light: #8f8f8f;
    --suit-dark: #4a4a4a;
    --badge-red: #b3262d;
    --badge-blue: #2a8fd0;
    --badge-navy: #1b4f8a;
    --badge-gold: #b8903f;
  }
  * { margin: 0; padding: 0; box-sizing: border-box; }
  html, body { width: 1200px; height: 900px; overflow: hidden; background: var(--ink-dark); }
  .ad {
    position: relative;
    width: 1200px;
    height: 900px;
    overflow: hidden;
    font-family: "Montserrat", sans-serif;
    color: var(--white);
  }
  .city-backdrop {
    position: absolute; inset: 0;
    background: linear-gradient(160deg, var(--city-top) 0%, #262626 45%, var(--city-bottom) 100%);
  }
  .brand {
    position: absolute; left: 96px; top: 136px; width: 620px;
    text-align: center;
  }
  .brand-name {
    display: flex; align-items: center; justify-content: center; gap: 18px;
    font-weight: 600; font-size: 56px; letter-spacing: 5px; color: var(--gold);
    line-height: 1; white-space: nowrap;
  }
  .brand-mark { width: 26px; height: 26px; background: var(--gold); flex: none; }
  .brand-tagline {
    margin-top: 12px;
    font-weight: 500; font-size: 20px; letter-spacing: 1px; color: var(--grey-text);
    white-space: nowrap;
  }
  .contact {
    position: absolute; right: 64px; top: 76px; text-align: right; font-style: normal;
  }
  .contact-phone { font-weight: 600; font-size: 35px; letter-spacing: 1px; line-height: 1.2; }
  .contact-web { font-weight: 500; font-size: 29px; color: var(--gold); line-height: 1.2; }
  .contact-address { margin-top: 14px; font-size: 22px; line-height: 28px; letter-spacing: .5px; }
  .practice-list {
    position: absolute; left: 90px; top: 260px; list-style: none;
  }
  .practice-list li {
    display: flex; align-items: center; height: 51.6px;
    font-weight: 500; font-size: 35px; letter-spacing: .5px; white-space: nowrap;
  }
  .practice-list li::before { content: "•"; font-size: 20px; margin-right: 14px; }
  .badge { position: absolute; }
  .badge-honor { left: 620px; top: 272px; width: 148px; height: 116px; }
  .badge-seal { left: 630px; top: 426px; width: 118px; height: 118px; }
  .badge-reviews { left: 90px; top: 568px; width: 130px; height: 92px; }
  .badge-rating { left: 294px; top: 556px; width: 120px; height: 112px; }
  .badge-accredit { left: 494px; top: 552px; width: 90px; height: 114px; }
  .trust-band {
    position: absolute; left: 0; top: 706px; width: 752px; height: 144px;
    background: var(--gold-band);
    padding: 28px 0 0 88px;
  }
  .trust-band p {
    font-style: italic; font-weight: 500; font-size: 35px; line-height: 44px;
    color: var(--band-text); letter-spacing: -.3px; white-space: nowrap;
  }
  .trust-band strong { font-weight: 800; }
  .attorney-photo {
    position: absolute; left: 736px; top: 256px; width: 464px; height: 644px;
    background: linear-gradient(180deg, #6a6a6a 0%, var(--suit-light) 40%, var(--suit-dark) 100%);
    clip-path: polygon(40% 0, 78% 0, 84% 38%, 100% 44%, 100% 100%, 0 100%, 4% 62%, 20% 46%, 38% 38%);
  }
  .name-plate {
    position: absolute; left: 710px; top: 802px; width: 490px; height: 68px;
  }
  .name-plate svg { position: absolute; inset: 0; }
  .name-plate span {
    position: absolute; right: 70px; top: 12px;
    font-family: "Tinos", serif; font-style: italic; font-weight: 700;
    font-size: 34px; color: var(--ink-dark); white-space: nowrap;
  }
</style>
</head>
<body>
<main class="ad">
  <div class="city-backdrop" role="img" aria-label="Dark aerial photograph of a downtown city skyline"></div>

  <header class="brand">
    <div class="brand-name"><span class="brand-mark"></span>MARVOLIN LAW</div>
    <div class="brand-tagline">SHAPING FAITH WITH RESULTS</div>
  </header>

  <address class="contact">
    <div class="contact-phone">310.555.0148</div>
    <div class="contact-web">marvolinlegal.com</div>
    <div class="contact-address">2180 Halvern Ave., Suite #402<br>Westbrook, CA 90417</div>
  </address>

  <ul class="practice-list">
    <li>Personal Injury</li>
    <li>Legal Malpractice</li>
    <li>Unlicensed Contractors</li>
    <li>Medical Malpractice</li>
    <li>Civil Litigation</li>
  </ul>

  <svg class="badge badge-honor" viewBox="0 0 148 116" role="img" aria-label="Attorney honor list badge">
    <rect x="4" y="6" width="140" height="104" rx="10" fill="var(--badge-gold)"/>
  </svg>
  <svg class="badge badge-seal" viewBox="0 0 118 118" role="img" aria-label="Trial advocates forum seal">
    <circle cx="59" cy="59" r="57" fill="var(--badge-red)"/>
    <circle cx="59" cy="59" r="36" fill="var(--badge-gold)"/>
  </svg>
  <svg class="badge badge-reviews" viewBox="0 0 130 92" role="img" aria-label="Five-star review site badge">
    <rect x="0" y="4" width="130" height="84" rx="8" fill="var(--badge-red)"/>
  </svg>
  <svg class="badge badge-rating" viewBox="0 0 120 112" role="img" aria-label="Top attorney rating badge">
    <circle cx="60" cy="56" r="54" fill="var(--badge-blue)"/>
    <circle cx="60" cy="56" r="42" fill="var(--white)"/>
  </svg>
  <svg class="badge badge-accredit" viewBox="0 0 90 114" role="img" aria-label="Accredited business badge">
    <rect x="2" y="2" width="86" height="110" rx="8" fill="var(--white)" stroke="var(--badge-navy)" stroke-width="3"/>
    <rect x="8" y="80" width="74" height="26" rx="4" fill="var(--badge-navy)"/>
  </svg>

  <section class="trust-band">
    <p>KNOWN AND TRUSTED IN OUR<br>COMMUNITY <strong>FOR OVER 22 YEARS</strong></p>
  </section>

  <div class="attorney-photo" role="img" aria-label="Portrait of attorney Gordon R. Marvolin in a grey suit and navy tie"></div>

  <div class="name-plate">
    <svg viewBox="0 0 490 68" preserveAspectRatio="none" aria-hidden="true">
      <polygon points="22,0 490,0 490,68 0,68" fill="var(--white)"/>
    </svg>
    <span>Gordon R. Marvolin, Esq.</span>
  </div>
</main>
</body>
</html>
```